Loomberry AI - Help users create their own recipe for a delicious AI treat!

Our company is an AI startup called Loomberrys. A Loomberry is an easy way to play with data (user can ask questions and get visualized answers about the dataset, sort of like QuillMate). Our users can "bake" their own Loomberrys by combining different sources of data.

We need a page that offers two things (both are required):

(1) TRY A LOOMBERRY --> Present a gallery of pre-made Loomberrys, each of which a user can click on and start playing with inside a popup iFrame. (visually, a Loomberry should be represented by some variation of our logo, attached). Designer does not need to worry about the iFrame popup.

(2) BAKE YOUR OWN LOOMBERRY --> Guide the user through making their own Loomberry recipe. The steps in making a Loomberry are:

A. Pick first ingredient - a Connector that imports the user's own data (visually, we present these options as logos for the Connector source, like Zentor, Pallomix, Brivane KLX, etc.).

B. Pick additional ingredients - the user can choose from 3rd-party cakes to combine with their own data added in (A). (visually, these 3rd-party cake options are presented as "mini" cakes, similar to our logo)

C. Once the ingredients are selected, the user can hit a BAKE button, and an iFrame popup opens, where user can play with the result. Designer does not need to worry about the iFrame popup.

We already have a web page and color scheme that we'd like this page to match (https://www.loomberrys.ai). The designer has freedom to play with format and try variations on the color scheme. The overall design should feel futuristic, fun, but also professional (like our logo).

Target Market(s)

Business users who want an easier way to get answers from large messy data

Industry/Entity Type

Tech/AI

Number of Pages Required

1 page

Font styles to use
Other font styles liked:
• Rubik

Requirements
Must have
• Full page design that matches current website (www.loomberrys.ai) and meets all requirements in the Project Description
Nice to have
• Included in the Project Description
Should not have
• Do not submit any designs that are too cartoonish or would not appeal to a business user

```html
<!DOCTYPE html>
<html lang="en">
<head>
<meta charset="utf-8">
<title>Loomberrys — Try or Bake a Loomberry</title>
<link href="https://fonts.googleapis.com/css2?family=Rubik:wght@400;500;600&family=Poppins:wght@400;500;600&display=swap" rel="stylesheet">
<style>
:root{
  --bg:#0e1028;
  --bg-deep:#0a0c20;
  --white:#ffffff;
  --muted:#c9cbe0;
  --faint:#7d80a3;
  --line:rgba(255,255,255,.55);
  --pink:#e0307f;
  --purple:#8a2d7a;
  --blue:#1d3a9e;
  --cyan:#18e0f0;
  --yellow:#ffe14a;
  --btn-blue:#1453b8;
  --btn-red:#ee1b24;
  --grad-warm:linear-gradient(90deg,#ffe14a,#f48bb8 55%,#18e0f0);
  --grad-block:linear-gradient(135deg,#f7b24a 0%,#e0568f 35%,#9a74d8 60%,#18e0f0 100%);
}
*{box-sizing:border-box;margin:0;padding:0}
html,body{width:1200px;height:4677px;overflow:hidden}
body{position:relative;background:var(--bg);color:var(--white);font-family:"Rubik",sans-serif}
.glow{position:absolute;border-radius:50%;filter:blur(90px);pointer-events:none}
.abs{position:absolute}
.nav-link{position:absolute;top:51px;font:500 12px "Poppins",sans-serif}
.brand{display:flex;align-items:center;gap:10px;font:400 28px "Rubik",sans-serif;color:var(--white)}
.brand-dot{width:22px;height:22px;border-radius:50%;background:var(--grad-warm)}
.btn-outline{position:absolute;border:1.5px solid var(--line);border-radius:30px;display:flex;align-items:center;justify-content:center;font:600 12px "Poppins",sans-serif;color:var(--white)}
.photo{position:absolute;overflow:hidden}
.section-title{position:absolute;left:0;width:1200px;text-align:center;font-weight:500}
.divider{position:absolute;left:546px;width:108px;height:2px;background:var(--muted)}
.cake-card{position:absolute;width:333px;height:238px;border:1.5px solid rgba(255,255,255,.7);border-radius:22px;background:rgba(12,13,30,.78);padding:0 26px}
.cake-mark{position:absolute;left:44px;top:44px;width:58px;height:58px;border-radius:12px;border:3px solid transparent;background:linear-gradient(var(--bg-deep),var(--bg-deep)) padding-box,var(--grad-warm) border-box}
.cake-q{position:absolute;left:26px;bottom:36px;right:26px;font:500 16px/1.4 "Poppins",sans-serif}
.step-label{position:absolute;font:500 11px "Poppins",sans-serif;letter-spacing:2px;color:var(--muted)}
.step-title{position:absolute;font:500 30px/1.15 "Rubik",sans-serif}
.step-text{position:absolute;font:400 12px/1.6 "Poppins",sans-serif;color:var(--muted)}
.pill{position:absolute;border-radius:20px;display:flex;align-items:center;justify-content:center;font:600 12px "Poppins",sans-serif}
.arch{position:absolute;border-radius:90px}
.block{position:absolute;border-radius:18px;background:var(--grad-block)}
.faq{position:absolute;left:329px;width:542px;border:1.5px solid rgba(255,255,255,.7);border-radius:6px;background:rgba(10,11,28,.6);font:600 10px "Poppins",sans-serif;padding:0 18px}
.faq-toggle{position:absolute;right:16px;width:22px;height:22px;border-radius:50%;background:var(--white);color:var(--bg);display:flex;align-items:center;justify-content:center;font:600 15px "Poppins",sans-serif}
.field{position:absolute;left:329px;width:542px;border:1.5px solid rgba(255,255,255,.55);border-radius:4px;font:400 10px "Poppins",sans-serif;color:var(--faint);padding:0 18px;display:flex;align-items:center;letter-spacing:.5px}
.foot-head{position:absolute;top:4475px;font:600 16px "Poppins",sans-serif}
.foot-link{position:absolute;font:400 11px "Poppins",sans-serif;color:var(--muted)}
.social{width:24px;height:24px;border:1.5px solid var(--white);border-radius:50%}
</style>
</head>
<body>

<!-- background glows -->
<div class="glow" style="left:450px;top:180px;width:600px;height:520px;background:#7a2a6e;opacity:.8"></div>
<div class="glow" style="left:820px;top:800px;width:480px;height:900px;background:#163a9a;opacity:.9"></div>
<div class="glow" style="left:-180px;top:2150px;width:650px;height:700px;background:#7d2767;opacity:.8"></div>
<div class="glow" style="left:820px;top:2500px;width:450px;height:800px;background:#163a9a;opacity:.8"></div>
<div class="glow" style="left:800px;top:3700px;width:500px;height:700px;background:#7a2a6e;opacity:.7"></div>
<div class="glow" style="left:-200px;top:3900px;width:500px;height:600px;background:#163a9a;opacity:.6"></div>

<!-- header -->
<header>
  <div class="brand abs" style="left:84px;top:40px">
    <span class="brand-dot"></span><span>loomberrys</span>
  </div>
  <a class="nav-link" style="left:434px">Home</a>
  <a class="nav-link" style="left:511px">About Us</a>
  <a class="nav-link" style="left:609px">Web Demo</a>
  <a class="nav-link" style="left:716px">Contact</a>
  <div class="btn-outline" style="left:958px;top:39px;width:158px;height:40px">Join the WaitList</div>
</header>

<!-- hero -->
<section class="hero">
  <p class="abs" style="left:84px;top:171px;font:500 12px 'Poppins',sans-serif">Welcome to Loomberrys!</p>
  <h1 class="abs" style="left:84px;top:212px;font:500 39px/53px 'Rubik',sans-serif">Does Your Company<br>Have Data That Others Would<br>Find Useful?</h1>
  <p class="abs" style="left:84px;top:436px;width:540px;font:400 12px/1.4 'Poppins',sans-serif">Explore our pre-made Loomberrys and dive into the world of data visualization. Click on any Loomberry below to start playing!</p>
  <div class="pill" style="left:84px;top:509px;width:175px;height:44px;border-radius:24px;background:var(--grad-warm);color:var(--bg);justify-content:flex-start;padding-left:14px;font-size:11px">TRY A LOOMBERRY
    <span style="position:absolute;right:14px;width:28px;height:28px;border-radius:50%;border:2px solid var(--white);display:flex;align-items:center;justify-content:center">
      <svg width="14" height="14" viewBox="0 0 14 14"><path d="M2 7h9M7 3l4 4-4 4" stroke="#fff" stroke-width="2" fill="none"/></svg>
    </span>
  </div>
  <div class="btn-outline" style="left:293px;top:509px;width:211px;height:44px;font-size:11px">BAKE YOUR OWN LOOMBERRY</div>
  <div class="photo" role="img" aria-label="Photo of a team reviewing data on computer screens" style="left:695px;top:325px;width:421px;height:268px;border-radius:10px;background:linear-gradient(135deg,#c9b8a8,#5b4a44 45%,#2a2f4a)">
    <svg class="abs" style="left:184px;top:108px" width="52" height="52" viewBox="0 0 52 52"><circle cx="26" cy="26" r="24" fill="rgba(255,255,255,.35)"/><path d="M21 16l14 10-14 10z" fill="#fff"/></svg>
  </div>
</section>

<!-- gallery -->
<section class="gallery">
  <h2 class="section-title" style="top:716px;font-size:26px;line-height:42px">Discover The Magic Of Data Visualization With Our Pre-Made Loomberrys.<br>Simply Click On A Loomberry Below To Start Exploring.</h2>
  <div class="divider" style="top:818px"></div>

  <div class="cake-card" style="left:84px;top:858px"><div class="cake-mark" style="left:44px"></div><p class="cake-q">Who are our repeat customers and how many times have they shopped with us?</p></div>
  <div class="cake-card" style="left:434px;top:858px"><div class="cake-mark"></div><p class="cake-q">Show me all outstanding invoices by due date</p></div>
  <div class="cake-card" style="left:783px;top:858px"><div class="cake-mark"></div><p class="cake-q">Show me all credit card expenses over $100</p></div>
  <div class="cake-card" style="left:84px;top:1126px"><div class="cake-mark"></div><p class="cake-q">Show me all credit card expenses over $100</p></div>
  <div class="cake-card" style="left:434px;top:1126px"><div class="cake-mark"></div><p class="cake-q">How much are our monthly expenses on average?</p></div>
  <div class="cake-card" style="left:783px;top:1126px"><div class="cake-mark"></div><p class="cake-q">What's the total amount invoiced by customer zip code?</p></div>

  <div class="btn-outline" style="left:537px;top:1409px;width:126px;height:30px;font-size:11px">View More</div>
</section>

<!-- bake your own -->
<section class="bake">
  <h2 class="section-title" style="top:1506px;font-size:38px">BAKE YOUR OWN LOOMBERRY</h2>
  <div class="divider" style="top:1582px"></div>

  <!-- step 1 -->
  <p class="step-label" style="left:153px;top:1692px">STEP- 1</p>
  <h3 class="step-title" style="left:153px;top:1724px">Pick First Ingredient</h3>
  <p class="step-text" style="left:153px;top:1782px;width:410px;font-size:11px">Choose a connector to import your own data seamlessly. Select from popular options:</p>
  <div class="pill" style="left:153px;top:1865px;width:164px;height:38px;background:var(--white);color:#3a4a80;font:500 20px 'Rubik',sans-serif">Zentor</div>
  <div class="pill" style="left:338px;top:1865px;width:164px;height:38px;background:var(--white);color:#111;font:500 20px 'Rubik',sans-serif">Brivane</div>
  <div class="pill" style="left:153px;top:1937px;width:164px;height:36px;background:var(--btn-blue)">Connect Your OWN</div>
  <div class="block" style="left:638px;top:1823px;width:390px;height:235px"></div>
  <div class="arch" role="img" aria-label="Dashboard screenshot with blue bar charts" style="left:608px;top:1636px;width:162px;height:324px;background:linear-gradient(180deg,#1d4a2c,#0a1020 25%,#0f2f6a 60%,#081022)"></div>
  <div class="arch" role="img" aria-label="Dashboard screenshot with cyan bar charts and metrics" style="left:793px;top:1686px;width:162px;height:322px;background:linear-gradient(180deg,#0a0d18,#0d5f70 45%,#0a1a22)"></div>

  <svg class="abs" style="left:460px;top:1985px" width="300" height="230" viewBox="0 0 300 230" fill="none" stroke="#fff" stroke-width="1.5"><path d="M16 6c-8 70 30 100 110 110s150 30 162 92"/><path d="M282 200l6 10 6-10"/></svg>

  <!-- step 2 -->
  <div class="block" style="left:202px;top:2330px;width:390px;height:235px;background:linear-gradient(315deg,#ffe14a,#e0568f 40%,#9a74d8 65%,#18e0f0)"></div>
  <div class="arch" role="img" aria-label="Photo of server racks with blue lights" style="left:153px;top:2165px;width:172px;height:375px;background:linear-gradient(180deg,#0b1a3a,#1a5fb8 50%,#06102a)"></div>
  <div class="arch" role="img" aria-label="Photo of server racks with blue lights" style="left:348px;top:2213px;width:172px;height:327px;background:linear-gradient(180deg,#0b1a3a,#1a5fb8 50%,#06102a)"></div>
  <p class="step-label" style="left:608px;top:2216px">STEP-2</p>
  <h3 class="step-title" style="left:608px;top:2242px;width:480px">Pick Additional Ingredients - 3rd-Party Cakes</h3>
  <p class="step-text" style="left:608px;top:2328px;width:440px;font-size:11px">Enhance your data with a variety of 3rd-party cakes. Mix and match to create your perfect recipe:</p>
  <div class="pill" style="left:608px;top:2415px;width:162px;height:37px;background:var(--btn-blue)">Civic Census</div>
  <div class="pill" style="left:797px;top:2415px;width:163px;height:37px;background:var(--btn-red)">Your Interest</div>

  <svg class="abs" style="left:460px;top:2525px" width="300" height="230" viewBox="0 0 300 230" fill="none" stroke="#fff" stroke-width="1.5"><path d="M286 4c4 60-20 100-110 108S22 130 16 212"/><path d="M10 202l6 10 6-10"/></svg>

  <!-- step 3 -->
  <p class="step-label" style="left:170px;top:2802px">STEP-3</p>
  <h3 class="step-title" style="left:170px;top:2826px">Ready To Bake!</h3>
  <p class="step-text" style="left:170px;top:2880px;width:430px;font-size:11px">Once you've selected your ingredients, hit the BAKE button, and watch the magic happen. An iFrame popup will open, allowing you to play with the delicious results.</p>
  <div class="pill" style="left:170px;top:2980px;width:175px;height:45px;border-radius:24px;background:var(--grad-warm);font:600 24px 'Rubik',sans-serif">BAKE</div>
  <div class="block" style="left:638px;top:2897px;width:390px;height:229px"></div>
  <div class="arch" role="img" aria-label="Photo of hands typing on a laptop" style="left:608px;top:2722px;width:172px;height:323px;background:linear-gradient(180deg,#eae6e2,#a7958a 50%,#4a3e3a)"></div>
  <div class="arch" role="img" aria-label="Photo of a laptop showing an analytics dashboard" style="left:808px;top:2770px;width:172px;height:325px;background:linear-gradient(180deg,#f2f2f4,#b8c6da 50%,#5b5a62)"></div>
</section>

<!-- faq -->
<section class="faqs">
  <p class="section-title" style="top:3205px;font:500 10px 'Poppins',sans-serif;letter-spacing:2px">FAQS</p>
  <h2 class="section-title" style="top:3228px;font-size:27px">Frequently asked questions . . .</h2>
  <div class="faq" style="top:3296px;height:147px">
    <p class="abs" style="left:18px;top:26px">How does Berrie work if I don't give her my data ?</p>
    <span class="faq-toggle" style="top:22px">−</span>
    <p class="abs" style="left:18px;top:74px;width:380px;font:400 9px/1.3 'Poppins',sans-serif">When you ask a question about structured data, the LLM can be very good at knowing how to answer the question.</p>
  </div>
  <div class="faq" style="top:3463px;height:45px"><p class="abs" style="left:18px;top:16px">How is Berrie different than QuillMate ?</p><span class="faq-toggle" style="top:11px">+</span></div>
  <div class="faq" style="top:3520px;height:45px"><p class="abs" style="left:18px;top:16px">How Accurate is Berrie ?</p><span class="faq-toggle" style="top:11px">+</span></div>
  <div class="btn-outline" style="left:538px;top:3601px;width:124px;height:30px;font-size:10px">View More FAQs</div>
</section>

<!-- contact -->
<section class="contact">
  <div class="abs" style="left:242px;top:3740px;width:716px;height:630px;border:1.5px solid rgba(255,255,255,.6);border-radius:26px"></div>
  <h2 class="section-title" style="top:3782px;font-size:28px">Get In Touch</h2>
  <div class="field" style="top:3862px;height:121px;align-items:flex-start;padding-top:18px">Question ? Feedback ? We Want It All.</div>
  <div class="field" style="top:4013px;height:53px">John Smith</div>
  <div class="field" style="top:4098px;height:53px">Email</div>
  <div class="field" style="top:4184px;height:53px">Describe your Organization
    <svg class="abs" style="right:18px;top:23px" width="10" height="6" viewBox="0 0 10 6"><path d="M0 0h10L5 6z" fill="#fff"/></svg>
  </div>
  <div class="pill" style="left:504px;top:4282px;width:192px;height:48px;border-radius:26px;background:linear-gradient(90deg,#1d3a9e,#e0568f);font:500 19px 'Rubik',sans-serif">Submit</div>
</section>

<!-- footer -->
<footer>
  <div class="abs" style="left:84px;top:4420px;width:1032px;height:1px;background:rgba(255,255,255,.18)"></div>
  <div class="brand abs" style="left:88px;top:4500px;font-size:38px">
    <span class="brand-dot" style="width:30px;height:30px"></span><span>loomberrys</span>
  </div>
  <div class="abs" style="left:182px;top:4577px;display:flex;gap:4px" aria-label="Picvale, Quipline, Pallomix">
    <span class="social"></span><span class="social"></span><span class="social"></span>
  </div>
  <p class="foot-head" style="left:608px">Quick Links</p>
  <p class="foot-head" style="left:783px">Services</p>
  <p class="foot-head" style="left:958px">Others</p>
  <a class="foot-link" style="left:608px;top:4514px">Home</a>
  <a class="foot-link" style="left:608px;top:4546px">About</a>
  <a class="foot-link" style="left:783px;top:4514px">Services</a>
  <a class="foot-link" style="left:783px;top:4546px">Services</a>
  <a class="foot-link" style="left:958px;top:4514px">Terms of Service</a>
  <a class="foot-link" style="left:958px;top:4546px">Privacy Policy</a>
  <a class="foot-link" style="left:958px;top:4577px;font-size:10px">Zentor API Disclosure</a>
  <p class="section-title" style="top:4632px;font:400 12px 'Poppins',sans-serif">© Company- All Rights Reserved</p>
</footer>

</body>
</html>
```